Label Design Project for my tea product Imported from Japan

I have a tea importing business. I want someone to help me design a label for my Uji matcha tea product. I want the label to be modern, neat, and beautifully designed. I prefer it to be easily adaptable to other tea products that I will be importing.
Product name: Organic Hoshiba Matcha
Company name: Calm Harbor Leaf Merchants
Description: Powdered Green Tea Matcha
Ceremonial grade premium quality
Directly imported from Japan
This product is going to be sold in the U.S. market, so please make sure that the label is in compliance with the BQC regulations.

Target Market(s)

High end tea consumers

Industry/Entity Type

Business

Requirements
Must have
• Marking of origin : product of Japan
• Imported by: Calm Harbor Leaf Merchants
• Leave space for Net weight, the name and place of business of the manufacturer.
• Ingredients: Green Tea 100%
• Nutrition list is not necessary.

```html
<!DOCTYPE html>
<html lang="en">
<head>
<meta charset="utf-8">
<title>Organic Hoshiba Matcha – Label</title>
<link rel="stylesheet" href="https://fonts.googleapis.com/css2?family=Lato:wght@300;400;700&family=Open+Sans:wght@600;700&display=swap">
<style>
  :root {
    --backdrop: #d4b498;
    --label-sage: #d3e3d9;
    --tab-mist: #f2f7f4;
    --tab-stitch: #d6e6dc;
    --tea-green: #3a9a5f;
    --logo-grey: #6f8a7a;
    --white: #ffffff;
  }
  * { margin: 0; padding: 0; box-sizing: border-box; }
  html, body { width: 1200px; height: 800px; overflow: hidden; }
  body {
    background: var(--backdrop);
    font-family: "Lato", Arial, sans-serif;
    position: relative;
  }
  .label {
    position: absolute;
    top: 62px;
    width: 408px;
    height: 678px;
    background: var(--label-sage);
    border-radius: 12px;
    --info-colour: var(--tea-green);
  }
  .label--green { left: 160px; }
  .label--white { left: 634px; --info-colour: var(--white); }

  .brand-tab {
    position: absolute;
    left: 45px;
    top: 0;
    width: 317px;
    height: 158px;
    background: var(--tab-mist);
    border-radius: 0 0 10px 10px;
  }
  .brand-tab::after {
    content: "";
    position: absolute;
    inset: 4px;
    border: 1.5px dashed var(--tab-stitch);
    border-top: none;
    border-radius: 0 0 8px 8px;
  }
  .brand-mark {
    position: absolute;
    top: 80px;
    left: 0;
    right: 0;
    display: flex;
    justify-content: center;
    align-items: center;
    gap: 7px;
    font-family: "Lato", Arial, sans-serif;
    font-weight: 300;
    font-size: 13px;
    letter-spacing: 0.5px;
    color: var(--logo-grey);
  }
  .brand-mark__dot {
    width: 9px; height: 9px; border-radius: 50%;
    background: var(--tea-green);
  }
  .brand-name {
    position: absolute;
    top: 123px;
    left: 0; right: 0;
    text-align: center;
    font-family: "Open Sans", Arial, sans-serif;
    font-weight: 700;
    font-size: 14.5px;
    color: var(--tea-green);
    letter-spacing: 0.2px;
  }

  .product-name {
    position: absolute;
    left: 44px;
    top: 632px;
    transform-origin: 0 0;
    transform: rotate(-90deg);
    white-space: nowrap;
    font-family: "Lato", Arial, sans-serif;
    font-weight: 700;
    font-size: 39px;
    line-height: 48px;
    color: var(--white);
    letter-spacing: 0;
  }

  .facts {
    position: absolute;
    right: 44px;
    top: 247px;
    padding-right: 4px;
    border-right: 1.5px solid var(--white);
    text-align: right;
    color: var(--info-colour);
    line-height: 1.2;
  }
  .facts__heading { font-size: 12px; }
  .facts__value { font-size: 16px; margin-bottom: 2px; }

  .importer-panel {
    position: absolute;
    left: 195px;
    right: 0;
    top: 580px;
    height: 58px;
    background: var(--tab-mist);
  }
  .cert-badge {
    position: absolute;
    left: 8px;
    top: 31px;
    width: 46px;
    height: 21px;
    border-radius: 4px;
    background: var(--tea-green);
  }
  .importer {
    position: absolute;
    left: 60px;
    right: 0;
    top: 3px;
    text-align: center;
    color: var(--tea-green);
  }
  .importer__heading { font-size: 8px; line-height: 10px; }
  .importer__mark {
    margin-top: 6px;
    font-weight: 300;
    font-size: 7px;
    color: var(--logo-grey);
    line-height: 10px;
  }
  .importer__name {
    margin-top: 6px;
    font-family: "Open Sans", Arial, sans-serif;
    font-weight: 700;
    font-size: 6px;
    line-height: 8px;
  }
</style>
</head>
<body>

  <article class="label label--green">
    <header class="brand-tab">
      <div class="brand-mark"><span class="brand-mark__dot"></span>CALM HARBOR LEAF MERCHANTS</div>
      <div class="brand-name">CALM HARBOR LEAF MERCHANTS</div>
    </header>
    <h1 class="product-name">Organic Hoshiba Matcha</h1>
    <dl class="facts">
      <dt class="facts__heading">Ingredients :</dt>
      <dd class="facts__value">Green Tea 100%</dd>
      <dt class="facts__heading">Marking of origin :</dt>
      <dd class="facts__value">Product of Japan</dd>
    </dl>
    <footer class="importer-panel">
      <span class="cert-badge" role="img" aria-label="Certification badge"></span>
      <div class="importer">
        <p class="importer__heading">Imported by :</p>
        <p class="importer__mark">CALM HARBOR LEAF MERCHANTS</p>
        <p class="importer__name">CALM HARBOR LEAF MERCHANTS</p>
      </div>
    </footer>
  </article>

  <article class="label label--white">
    <header class="brand-tab">
      <div class="brand-mark"><span class="brand-mark__dot"></span>CALM HARBOR LEAF MERCHANTS</div>
      <div class="brand-name">CALM HARBOR LEAF MERCHANTS</div>
    </header>
    <h1 class="product-name">Organic Hoshiba Matcha</h1>
    <dl class="facts">
      <dt class="facts__heading">Ingredients :</dt>
      <dd class="facts__value">Green Tea 100%</dd>
      <dt class="facts__heading">Marking of origin :</dt>
      <dd class="facts__value">Product of Japan</dd>
    </dl>
    <footer class="importer-panel">
      <span class="cert-badge" role="img" aria-label="Certification badge"></span>
      <div class="importer">
        <p class="importer__heading">Imported by :</p>
        <p class="importer__mark">CALM HARBOR LEAF MERCHANTS</p>
        <p class="importer__name">CALM HARBOR LEAF MERCHANTS</p>
      </div>
    </footer>
  </article>

</body>
</html>
```